Financial Planning Firm needs a client data collection summary sheet to print on A3

We are a financial advice company, and we are after a 1-page sheet where we can write all of the client’s personal information in our meetings, like a mind map.
It should have our logo on the page along with a place to put the Client's Name and the Date.
It also needs to have the following Headings
Family
Home
Investments
Business
Estate Plan
Lifestyle
Money
Retirement
Dreams & Goals
Health and Wellbeing
It also needs to have our License details on the bottom: Tellora Counsel Pty Ltd (538216) is an Authorised Representative of Brindle Estate Capital Group Pty Ltd AFSL No: 613985 ABN 57 218 964 402. This document has been prepared by Tellora Counsel and is for general information only.
Please utilise our colour scheme as per our logo attached. Please find uploaded to the project an example data collection summary sheet that we use currently.

```html
<!DOCTYPE html>
<html lang="en">
<head>
<meta charset="utf-8">
<title>Tellora Counsel – Client Summary Sheet</title>
<link rel="stylesheet" href="https://fonts.googleapis.com/css2?family=Montserrat:wght@300;400;500;600&display=swap">
<style>
  :root {
    --ink: #000000;
    --paper: #ffffff;
    --gold: #c49a6c;
    --gold-soft: #ead9c4;
    --rule: #333333;
    --text: #111111;
  }
  * { box-sizing: border-box; margin: 0; padding: 0; }
  html, body {
    width: 1200px; height: 849px; overflow: hidden;
    background: var(--paper);
    font-family: "Montserrat", Arial, sans-serif;
    color: var(--text);
  }
  .sheet { position: relative; width: 1200px; height: 849px; }

  .masthead {
    position: absolute; left: 0; top: 0; width: 100%; height: 166px;
    background: var(--ink); color: var(--paper);
    text-align: center;
  }
  .brand-name {
    position: absolute; left: 0; right: 0; top: 46px;
    font-size: 40px; font-weight: 500; letter-spacing: 6px;
    text-transform: uppercase; line-height: 1;
  }
  .tagline {
    position: absolute; left: 0; right: 0; top: 104px;
    display: flex; align-items: center; justify-content: center; gap: 14px;
    font-size: 17px; font-weight: 300; letter-spacing: 6px;
  }
  .tagline::before, .tagline::after {
    content: ""; display: block; width: 50px; height: 1px; background: var(--paper);
  }

  .field { position: absolute; top: 212px; font-size: 12px; font-weight: 500; }
  .field-line { position: absolute; top: 271px; height: 1px; background: var(--rule); }
  .field--name { left: 80px; }
  .field-line--name { left: 80px; width: 342px; }
  .field--date { left: 449px; }
  .field-line--date { left: 450px; width: 124px; }

  .topic {
    position: absolute; width: 200px; margin-left: -100px;
    text-align: center;
  }
  .topic-icon {
    display: block; margin: 0 auto;
    width: 74px; height: 66px; border-radius: 8px;
    background: linear-gradient(160deg, var(--gold-soft), #f5ece1);
  }
  .topic-label {
    margin-top: 30px; font-size: 21px; font-weight: 400; line-height: 1.02;
    letter-spacing: 0.3px;
  }
  .row-1 { top: 366px; }
  .row-2 { top: 566px; }
  .col-1 { left: 184px; } .col-2 { left: 392px; } .col-3 { left: 600px; }
  .col-4 { left: 808px; } .col-5 { left: 1015px; }

  .licence {
    position: absolute; left: 0; right: 0; top: 804px;
    text-align: center; font-size: 9.6px; font-weight: 600;
  }
</style>
</head>
<body>
<main class="sheet">
  <header class="masthead">
    <div class="brand-name">Tellora Counsel</div>
    <div class="tagline">YOUR FINANCIAL EXPERT</div>
  </header>

  <span class="field field--name">Name</span>
  <span class="field-line field-line--name"></span>
  <span class="field field--date">Date</span>
  <span class="field-line field-line--date"></span>

  <section class="topic row-1 col-1"><span class="topic-icon" role="img" aria-label="Line icon of a heart holding a family"></span><p class="topic-label">family</p></section>
  <section class="topic row-1 col-2"><span class="topic-icon" role="img" aria-label="Line icon of a house beside a tree"></span><p class="topic-label">home</p></section>
  <section class="topic row-1 col-3"><span class="topic-icon" role="img" aria-label="Line icon of a plant growing a coin"></span><p class="topic-label">investments</p></section>
  <section class="topic row-1 col-4"><span class="topic-icon" role="img" aria-label="Line icon of a globe with a briefcase"></span><p class="topic-label">business</p></section>
  <section class="topic row-1 col-5"><span class="topic-icon" role="img" aria-label="Line icon of a property document and pen"></span><p class="topic-label">estate plan</p></section>

  <section class="topic row-2 col-1"><span class="topic-icon" role="img" aria-label="Line icon of a sofa"></span><p class="topic-label">lifestyle</p></section>
  <section class="topic row-2 col-2"><span class="topic-icon" role="img" aria-label="Line icon of a wallet and coins"></span><p class="topic-label">money</p></section>
  <section class="topic row-2 col-3"><span class="topic-icon" role="img" aria-label="Line icon of a sun over mountains"></span><p class="topic-label">retirement</p></section>
  <section class="topic row-2 col-4"><span class="topic-icon" role="img" aria-label="Line icon of a target with an arrow"></span><p class="topic-label">dreams<br>and goals</p></section>
  <section class="topic row-2 col-5"><span class="topic-icon" role="img" aria-label="Line icon of a stethoscope"></span><p class="topic-label">health<br>and wellbeing</p></section>

  <footer class="licence">Tellora Counsel Pty Ltd (538216) is an Authorised Representative of Brindle Estate Capital Group Pty Ltd AFSL No: 613985 ABN 57 218 964 402. This document has been prepared by Tellora Counsel and is for general information only.</footer>
</main>
</body>
</html>
```